School District In Need of Powerful Presentation

Create a modern PPT design template -- standard and widescreen -- for the Pell RU-8K school district inspired by its logo. The presentation should be a modern projection of 21st education that excites the people who view it. The school district is located in a rural farming community with a view of the rocky mountains to its west (check out this picture www.campsiteatmarblefork.example/AnimatedImages/HomeGallery/000MountainScene.jpg). People in this community want quality education for their children with opportunities for them to be successful after they graduate.

Target Market(s)

The Harbrook and Denning communities in Northern Colorado

Industry/Entity Type

Education

Font styles to use
Sans Serif

Colors
ec1f27
3176b5
acd036
fece3e
f78f20

Requirements
Must have
• The name of the school district:
• Pell County School District RU-8K Harbrook-Denning
• Website address: www.pellru8k.example/
• Email: listen@pellru8k.example
Nice to have
• A couple of color options including their current color scheme: red, gold, black
• Placeholder for pictures of students and teachers
Should not have
• Please do not use the full logo in it's current for, but you may use elements of the logo.

```html
<!DOCTYPE html>
<html lang="en">
<head>
<meta charset="utf-8">
<title>Pell County School District RU-8K – Future Vision</title>
<link rel="stylesheet" href="https://fonts.googleapis.com/css2?family=Oswald:wght@700&family=Open+Sans:wght@400;600&display=swap">
<style>
:root{
  --red:#ec1f27; --red-deep:#d20a11; --blue:#3176b5; --green:#acd036; --green-deep:#8cbf00;
  --gold:#fece3e; --orange:#f78f20; --teal:#1ea0c8; --ink:#1f1f1f; --board:#1e1e1e;
  --wood:#b5541c; --ledge:#6d6d6d; --slide:#ececec; --page:#f6f6f6; --line:#7a7a7a;
}
*{margin:0;padding:0;box-sizing:border-box}
html,body{width:1200px;height:1018px;overflow:hidden;background:var(--page)}
.stage{position:absolute;left:0;top:0;width:1500px;height:1272px;transform:scale(.8);transform-origin:0 0;font-family:"Open Sans",sans-serif;color:var(--ink)}
.slide{position:absolute;left:18px;top:75px;width:1460px;height:1127px;background:var(--slide)}
.abs{position:absolute}
.heading{position:absolute;font-family:"Oswald",sans-serif;font-weight:700;text-transform:uppercase;text-align:center;line-height:31px;font-size:26px;letter-spacing:-.3px;white-space:nowrap;transform:scaleX(.84);transform-origin:50% 50%}
/* chalkboard */
.board-frame{left:68px;top:97px;width:772px;height:248px;background:var(--wood);border-radius:3px}
.board{left:80px;top:108px;width:748px;height:230px;background:var(--board);border-radius:2px}
.ledge{left:55px;top:344px;width:796px;height:11px;background:var(--ledge);border-radius:4px}
.board-text{position:absolute;width:748px;left:80px;text-align:center;color:#fff;white-space:nowrap}
.board-title{top:116px;font-size:28px}
.board-sub{top:154px;font-size:22px}
.board-contact{top:199px;font-size:22px;left:130px;width:auto;display:flex;gap:54px;align-items:center}
.board-contact span{display:flex;align-items:center;gap:6px}
.board-tagline{top:292px;font-size:26px}
.dot{position:absolute;top:247px;width:34px;height:34px;border-radius:50%}
/* student goals */
.goal-spine{left:55px;top:398px;width:80px;height:367px;background:var(--gold);border-radius:40px}
.goal-spine-text{position:absolute;left:95px;top:581px;transform:translate(-50%,-50%) rotate(-90deg);white-space:nowrap;font-size:22px;line-height:31px;text-align:center;color:var(--ink)}
.goal-link{position:absolute;left:135px;width:80px;height:6px;background:var(--gold)}
.goal{position:absolute;left:186px;width:466px;height:76px;border-radius:38px;color:#fff;font-size:19px;line-height:27px;display:flex;align-items:center;padding-left:83px}
.badge{position:absolute;width:44px;height:44px;border-radius:50%;background:#fff;border:3px solid var(--gold);font-family:"Oswald",sans-serif;font-weight:700;font-size:24px;color:var(--ink);display:flex;align-items:center;justify-content:center}
.goal .badge{left:24px;top:16px}
/* actions table */
.actions{left:53px;top:930px;width:672px;height:238px;display:flex}
.action{flex:1;background:#fff;text-align:center;font-size:16.5px;line-height:22px;position:relative}
.action-head{height:58px;color:#fff;font-family:"Oswald",sans-serif;font-weight:700;font-size:26px;display:flex;align-items:center;justify-content:center}
.action svg{margin:12px auto 2px;display:block}
.action-foot{position:absolute;left:0;right:0;bottom:0;height:6px}
/* aspire */
.ribbon{position:absolute;top:394px;width:122px;height:212px}
.ribbon-text{position:absolute;left:20px;width:82px;top:72px;text-align:center;font-size:10px;line-height:13px;color:var(--ink)}
.ribbon .badge{left:39px;top:6px;border:none;width:44px;height:44px;font-size:26px}
.aspire-text{left:1022px;top:198px;width:240px;font-size:30px;line-height:34px}
/* needs */
.tag{position:absolute;top:720px;width:114px;height:58px;color:#fff;font-size:16.5px;text-align:center;padding-top:5px}
.list{position:absolute;list-style:none;font-size:16.5px;line-height:22px}
.list li{position:relative;padding-left:13px;margin-bottom:8px}
.list li::before{content:"";position:absolute;left:0;top:9px;width:6px;height:6px;border-radius:50%;background:var(--bullet)}
.ready{left:803px;top:1023px;width:640px;height:147px}
.ready-list{position:absolute;left:816px;top:1032px;list-style:none;font-size:16.5px;line-height:26px}
.ready-list li::before{content:"● ";font-size:12px;vertical-align:1px}
</style>
</head>
<body>
<div class="stage">
  <div class="slide"></div>

  <!-- chalkboard -->
  <div class="abs board-frame"></div>
  <div class="abs board"></div>
  <div class="abs ledge"></div>
  <div class="board-text board-title">PELL COUNTY SCHOOL</div>
  <div class="board-text board-sub">DISTRICT RU-8K HARBROOK-DENNING</div>
  <div class="board-text board-contact">
    <span><svg width="20" height="20" viewBox="0 0 20 20" fill="none" stroke="#fff" stroke-width="1.5"><circle cx="10" cy="10" r="8"/><ellipse cx="10" cy="10" rx="3.5" ry="8"/><path d="M2 10h16M4 5.5h12M4 14.5h12"/></svg>www.pellru8k.example/</span>
    <span><svg width="24" height="18" viewBox="0 0 24 18"><rect x="1" y="1" width="22" height="16" fill="#fff"/><path d="M1 1l11 9 11-9" fill="none" stroke="#1e1e1e" stroke-width="1.6"/></svg>listen@pellru8k.example</span>
  </div>
  <div class="dot" style="left:189px;background:var(--blue)"></div>
  <div class="dot" style="left:243px;background:var(--teal)"></div>
  <div class="dot" style="left:296px;background:var(--green)"></div>
  <div class="dot" style="left:349px;background:var(--gold)"></div>
  <div class="dot" style="left:403px;background:var(--red)"></div>
  <div class="dot" style="left:461px;background:var(--blue)"></div>
  <div class="dot" style="left:515px;background:var(--teal)"></div>
  <div class="dot" style="left:568px;background:var(--green)"></div>
  <div class="dot" style="left:622px;background:var(--gold)"></div>
  <div class="dot" style="left:676px;background:var(--red)"></div>
  <div class="board-text board-tagline">What we want the future to hold for our students</div>

  <!-- student goals -->
  <div class="abs goal-spine"></div>
  <div class="goal-spine-text">WE WANT PELL RU-8K<br>STUDENTS TO BE</div>
  <div class="goal-link" style="top:430px"></div>
  <div class="goal-link" style="top:527px"></div>
  <div class="goal-link" style="top:625px"></div>
  <div class="goal-link" style="top:723px"></div>
  <div class="goal" style="top:396px;background:var(--blue)"><span class="badge">A</span>Able to achieve high expectations.</div>
  <div class="goal" style="top:493px;background:var(--orange)"><span class="badge">B</span>Life-long learners.</div>
  <div class="goal" style="top:591px;background:var(--green-deep)"><span class="badge">C</span>Set up for success, prepared for</div>
  <div class="goal" style="top:689px;background:var(--red-deep)"><span class="badge">D</span>Proud of where they came from and<br>where they went to school.</div>

  <!-- actions -->
  <div class="heading" style="left:-14px;top:856px;width:800px">What we need to do now to prepare Pell RU-8K students<br>for this future we envision</div>
  <div class="abs actions">
    <div class="action"><div class="action-head" style="background:var(--blue)">A</div>
      <svg width="38" height="34" viewBox="0 0 38 34"><rect x="1" y="1" width="24" height="16" rx="2" fill="var(--blue)"/><path d="M6 17l-2 6 7-6z" fill="var(--blue)"/><rect x="12" y="12" width="24" height="16" rx="2" fill="#5c9bd6"/><path d="M30 28l3 5-8-5z" fill="#5c9bd6"/><path d="M16 17h16M16 21h16M16 25h10" stroke="#fff" stroke-width="1.6"/></svg>
      Shine a<br>light on our<br>students<br>&amp; schools.<div class="action-foot" style="background:var(--blue)"></div></div>
    <div class="action"><div class="action-head" style="background:var(--green-deep)">B</div>
      <svg width="44" height="34" viewBox="0 0 44 34"><path d="M2 10l10-4 10 5 10-5 10 4-4 12-8 6-8-5-8 5-8-6z" fill="var(--green-deep)"/><path d="M14 16l6 5 4-2 6 5" stroke="#fff" stroke-width="1.6" fill="none"/></svg>
      Cultivate a<br>collaborative<br>culture.<div class="action-foot" style="background:var(--green-deep)"></div></div>
    <div class="action"><div class="action-head" style="background:var(--orange)">C</div>
      <svg width="38" height="34" viewBox="0 0 38 34"><path d="M2 4c6-2 12-1 16 3v24c-4-3-10-4-16-2z" fill="var(--orange)"/><path d="M36 4c-6-2-12-1-16 3v24c4-3 10-4 16-2z" fill="var(--orange)"/><path d="M6 10h8M6 15h8M24 10h8M24 15h8" stroke="#fff" stroke-width="1.4"/></svg>
      Align<br>curriculum,<br>instruction, &amp;<br>professional<br>development<div class="action-foot" style="background:var(--orange)"></div></div>
    <div class="action"><div class="action-head" style="background:var(--gold)">D</div>
      <svg width="38" height="34" viewBox="0 0 38 34"><path d="M33 2v30H3z" fill="none" stroke="var(--gold)" stroke-width="2"/></svg>
      Conduct<br>continuous<br>improvement<br>conversations.<div class="action-foot" style="background:var(--gold)"></div></div>
    <div class="action"><div class="action-head" style="background:var(--red-deep)">E</div>
      <svg width="42" height="34" viewBox="0 0 42 34" fill="var(--red-deep)"><circle cx="21" cy="6" r="5"/><circle cx="10" cy="12" r="4.5"/><circle cx="32" cy="12" r="4.5"/><path d="M13 24c0-7 16-7 16 0v6H13z"/><path d="M2 28c0-6 13-7 14-2v6H2zM40 28c0-6-13-7-14-2v6h14z"/></svg>
      Energize and<br>engage our<br>entire<br>community<div class="action-foot" style="background:var(--red-deep)"></div></div>
  </div>

  <!-- aspire circle and connectors -->
  <svg class="abs" style="left:0;top:0" width="1500" height="420" viewBox="0 0 1500 420">
    <g fill="none" stroke="var(--line)" stroke-width="2">
      <path d="M988 165H905V395"/><path d="M1297 165H1378V395"/><path d="M1065 353V395"/><path d="M1220 353V395"/>
    </g>
    <g fill="var(--line)"><circle cx="988" cy="165" r="7"/><circle cx="1297" cy="165" r="7"/><circle cx="1065" cy="353" r="7"/><circle cx="1220" cy="353" r="7"/></g>
    <g fill="none" stroke-width="20">
      <path d="M1142 110A120 120 0 0 1 1262 230" stroke="var(--blue)"/>
      <path d="M1262 230A120 120 0 0 1 1142 350" stroke="var(--gold)"/>
      <path d="M1142 350A120 120 0 0 1 1022 230" stroke="var(--green)"/>
      <path d="M1022 230A120 120 0 0 1 1142 110" stroke="var(--red)"/>
    </g>
    <circle cx="1142" cy="230" r="110" fill="#fff"/>
    <circle cx="1142" cy="230" r="104" fill="#e5e9ee"/>
  </svg>
  <div class="heading aspire-text">We aspire to be<br>a district that</div>

  <div class="ribbon" style="left:843px">
    <svg width="122" height="212" viewBox="0 0 122 212"><path d="M0 0h122v140l-15 8H15L0 140z" fill="var(--red)"/><path d="M15 62h92v110l-46 22-46-22z" fill="#fde8e8"/><path d="M15 162l46 22 46-22v14l-46 22-46-22zM15 186l46 22 46-22v-10l-46 22" fill="var(--red)"/><g fill="var(--red)"><circle cx="34" cy="150" r="3"/><circle cx="52" cy="150" r="3"/><circle cx="70" cy="150" r="3"/><circle cx="88" cy="150" r="3"/></g></svg>
    <span class="badge">A</span><div class="ribbon-text">Is guided by shared goals and a shared vision for educating our children.</div></div>
  <div class="ribbon" style="left:1004px">
    <svg width="122" height="212" viewBox="0 0 122 212"><path d="M0 0h122v140l-15 8H15L0 140z" fill="var(--green)"/><path d="M15 62h92v110l-46 22-46-22z" fill="#eef5dc"/><path d="M15 162l46 22 46-22v14l-46 22-46-22zM15 186l46 22 46-22v-10l-46 22" fill="var(--green)"/><g fill="var(--green)"><circle cx="34" cy="150" r="3"/><circle cx="52" cy="150" r="3"/><circle cx="70" cy="150" r="3"/><circle cx="88" cy="150" r="3"/></g></svg>
    <span class="badge">B</span><div class="ribbon-text">Demonstrates excellence at every level.</div></div>
  <div class="ribbon" style="left:1161px">
    <svg width="122" height="212" viewBox="0 0 122 212"><path d="M0 0h122v140l-15 8H15L0 140z" fill="var(--gold)"/><path d="M15 62h92v110l-46 22-46-22z" fill="#f7efd9"/><path d="M15 162l46 22 46-22v14l-46 22-46-22zM15 186l46 22 46-22v-10l-46 22" fill="var(--gold)"/><g fill="var(--gold)"><circle cx="34" cy="150" r="3"/><circle cx="52" cy="150" r="3"/><circle cx="70" cy="150" r="3"/><circle cx="88" cy="150" r="3"/></g></svg>
    <span class="badge">C</span><div class="ribbon-text">Is fiscal and resource-<br>responsible.</div></div>
  <div class="ribbon" style="left:1320px">
    <svg width="122" height="212" viewBox="0 0 122 212"><path d="M0 0h122v140l-15 8H15L0 140z" fill="var(--blue)"/><path d="M15 62h92v110l-46 22-46-22z" fill="#e3eef9"/><path d="M15 162l46 22 46-22v14l-46 22-46-22zM15 186l46 22 46-22v-10l-46 22" fill="var(--blue)"/><g fill="var(--blue)"><circle cx="34" cy="150" r="3"/><circle cx="52" cy="150" r="3"/><circle cx="70" cy="150" r="3"/><circle cx="88" cy="150" r="3"/></g></svg>
    <span class="badge">D</span><div class="ribbon-text">Seeks and invests in the most capable and talented staff.</div></div>

  <!-- classroom & home -->
  <div class="heading" style="left:717px;top:652px;width:800px">What our students need to be doing in their classrooms<br>and at home</div>
  <svg class="abs" style="left:800px;top:680px" width="660" height="270" viewBox="800 680 660 270">
    <g stroke="#222" stroke-width="2" fill="none"><path d="M908 688H970M938 688V720M1258 688H1322M1290 688V720"/></g>
    <path d="M1120 785V940" stroke="#d6d6d6" stroke-width="1.5"/>
    <path d="M880 720h113v30l-56 28-57-28z" fill="var(--blue)"/>
    <path d="M1232 720h114v30l-57 28-57-28z" fill="var(--red)"/>
  </svg>
  <div class="tag" style="left:880px">CLASSROOM</div>
  <div class="tag" style="left:1232px">HOME</div>
  <ul class="list" style="left:803px;top:784px;--bullet:var(--blue)">
    <li>Gaining 21st century skills.</li>
    <li>Owning their learning and<br>educational experience; knowing<br>what success is and how to achieve it.</li>
    <li>Embracing challenges.</li>
    <li>Encouraged to set ambitious goals.</li>
  </ul>
  <ul class="list" style="left:1147px;top:784px;--bullet:var(--red)">
    <li>Understanding the value of education.</li>
    <li>Feeling their parents/family are<br>engaged in their education.</li>
    <li>Being encouraged and supported to<br>reach their goals.</li>
    <li>Taking pride in their community.</li>
  </ul>

  <!-- get ready -->
  <div class="heading" style="left:717px;top:981px;width:800px">What our schools need to do to get ready</div>
  <svg class="abs ready" viewBox="0 0 640 147"><path d="M0 0h577l63 73-63 74H0z" fill="var(--green)"/></svg>
  <ul class="ready-list">
    <li>Improve student achievement.</li>
    <li>Collaborate.</li>
    <li>Embrace a growth mindset.</li>
    <li>Work with students and their families to identify and set goals.</li>
    <li>Address the distinct learning needs,interests, and aspirations of students.</li>
  </ul>
</div>
</body>
</html>
```